Very personalised Wedding Invitation

I want a wedding invitation very unique and personalised with the menus, ceremony time table and thank you cards. I want a mix of a nice traditional style with indian style touch. I don't want a colourful invitation, it can have max. two different colours.

The bride's name is Miranda and the groom's name is Rohan

Reason: None of the designs submitted are what I am looking for

Target Market(s)

Invitations, personalised invitations,

Industry/Entity Type

Wedding

Logo Text

Our initials R&M To use in our wedding things

Font styles to use
Decorative
Script

Requirements
Must have
• -
Nice to have
• I would like a chic design with a bit of indian style
Should not have
• --

```html
<!DOCTYPE html>
<html lang="en">
<head>
<meta charset="utf-8">
<title>Miranda &amp; Rohan — Wedding Stationery</title>
<link rel="stylesheet" href="https://fonts.googleapis.com/css2?family=Dancing+Script:wght@500&family=Kaushan+Script&family=Open+Sans:wght@400&display=swap">
<style>
  :root {
    --backdrop: #e6dfd4;
    --paper: #ffffff;
    --blush: #f39bb0;
    --blush-soft: #f7b8c6;
    --blush-pale: #fbe1e7;
    --cocoa: #a88a73;
    --cocoa-pale: #dccbbd;
    --ink: #4a3a30;
    --rule: #e3cdb9;
    --shadow: rgba(80, 60, 40, 0.16);
  }
  * { margin: 0; padding: 0; box-sizing: border-box; }
  html, body { width: 1200px; height: 983px; overflow: hidden; }
  body {
    position: relative;
    background: var(--backdrop);
    font-family: "Open Sans", Arial, sans-serif;
    color: var(--ink);
  }
  .card {
    position: absolute;
    background: var(--paper);
    box-shadow: 0 10px 14px -8px var(--shadow);
  }
  .arch-frame { position: absolute; left: 0; top: 0; pointer-events: none; }
  .floral { position: absolute; border-radius: 50%; }
  .floral--bouquet {
    background: radial-gradient(ellipse at 50% 48%, var(--blush) 0%, var(--blush-soft) 26%, var(--cocoa-pale) 50%, rgba(220,203,189,0.35) 66%, rgba(255,255,255,0) 74%);
  }
  .floral--sprig {
    background: radial-gradient(ellipse at 50% 50%, var(--cocoa-pale) 0%, rgba(220,203,189,0.45) 48%, rgba(255,255,255,0) 72%);
  }
  .script-pink {
    font-family: "Dancing Script", cursive;
    color: var(--blush);
    text-align: center;
    line-height: 0.86;
    font-weight: 500;
  }
  .script-cocoa {
    font-family: "Kaushan Script", cursive;
    color: var(--cocoa);
    text-align: center;
    font-weight: 400;
  }

  /* Invitation */
  .invitation { left: 89px; top: 68px; width: 583px; height: 824px; }
  .invitation .floral--bouquet { left: 67px; top: 34px; width: 474px; height: 222px; }
  .invitation__headline { position: absolute; left: 0; width: 100%; top: 236px; font-size: 74px; }
  .invitation__couple { position: absolute; left: 0; width: 100%; top: 450px; font-size: 44px; line-height: 1; }
  .invitation__intro { position: absolute; left: 0; width: 100%; top: 529px; font-size: 15px; line-height: 21px; text-align: center; }
  .invitation .floral--sprig { left: 240px; top: 586px; width: 104px; height: 70px; }
  .invitation__details { position: absolute; left: 0; width: 100%; top: 687px; font-size: 15px; line-height: 19.5px; text-align: center; }
  .invitation__after { position: absolute; left: 0; width: 100%; top: 751px; font-size: 16px; text-align: center; }
  .timetable {
    position: absolute; left: 0; width: 100%; top: 784px;
    display: flex; justify-content: center; gap: 22px;
    list-style: none; font-size: 12px; color: var(--cocoa);
  }
  .timetable__time { font-weight: 400; color: var(--blush); margin-right: 4px; }

  /* Menu */
  .menu { left: 714px; top: 68px; width: 384px; height: 546px; }
  .menu__title { position: absolute; left: 0; width: 100%; top: 22px; font-size: 54px; line-height: 0.95; }
  .menu__courses { position: absolute; left: 90px; width: 204px; top: 154px; list-style: none; }
  .menu__course {
    height: 63.5px;
    padding-top: 12px;
    font-size: 12px;
    text-align: center;
    border-bottom: 1px dashed var(--rule);
  }
  .menu .floral--bouquet { left: 96px; top: 424px; width: 192px; height: 84px; }

  /* Gift tag */
  .tag { position: absolute; width: 150px; height: 240px; }
  .tag--back { left: 784px; top: 664px; background: var(--blush-soft); transform: rotate(3deg); clip-path: polygon(22% 0, 78% 0, 100% 14%, 100% 100%, 0 100%, 0 14%); }
  .tag__monogram {
    position: absolute; right: 12px; bottom: 14px;
    width: 46px; height: 46px; border-radius: 50%;
    border: 1px solid var(--paper);
    font-family: "Kaushan Script", cursive; font-size: 16px; line-height: 44px;
    color: var(--paper); text-align: center;
  }
  .tag--front { left: 716px; top: 652px; background: var(--paper); transform: rotate(17deg); box-shadow: 0 8px 12px -6px var(--shadow); clip-path: polygon(22% 0, 78% 0, 100% 14%, 100% 100%, 0 100%, 0 14%); }
  .tag__hole { position: absolute; left: 69px; top: 14px; width: 12px; height: 12px; border-radius: 50%; background: var(--backdrop); }
  .tag__headline { position: absolute; left: 0; width: 100%; top: 38px; font-size: 40px; }
  .tag .floral--sprig { left: 18px; top: 150px; width: 62px; height: 46px; }
  .tag__bow { position: absolute; left: 796px; top: 640px; width: 62px; height: 48px; }

  /* Thank-you card */
  .thanks { left: 958px; top: 674px; width: 140px; height: 220px; }
  .thanks__title { position: absolute; left: 0; width: 100%; top: 36px; font-size: 34px; line-height: 0.95; }
  .thanks .floral--bouquet { left: 16px; top: 146px; width: 110px; height: 54px; }
</style>
</head>
<body>

<section class="card invitation">
  <svg class="arch-frame" width="583" height="824" viewBox="0 0 583 824" aria-hidden="true">
    <path d="M20 804 V180 C20 120 190 98 291.5 22 C393 98 563 120 563 180 V804 Z" fill="none" stroke="var(--cocoa-pale)" stroke-width="1.2"/>
    <path d="M28 796 V184 C28 128 194 106 291.5 32 C389 106 555 128 555 184 V796 Z" fill="none" stroke="var(--blush-pale)" stroke-width="1"/>
  </svg>
  <div class="floral floral--bouquet" role="img" aria-label="Watercolour bouquet of pink roses with leaves"></div>
  <h1 class="script-pink invitation__headline">Save<br>the<br>Date</h1>
  <h2 class="script-cocoa invitation__couple">Miranda &amp; Rohan</h2>
  <p class="invitation__intro">We are getting<br>married</p>
  <div class="floral floral--sprig" role="img" aria-label="Watercolour leaf sprig"></div>
  <p class="invitation__details">Sunday 17 may 2015,<br>at six o'clock in the afternoon<br>San Francisco, California</p>
  <p class="invitation__after">Dinner and dancing to follow</p>
  <ul class="timetable">
    <li><span class="timetable__time">6 pm</span>Ceremony</li>
    <li><span class="timetable__time">7 pm</span>Dinner</li>
    <li><span class="timetable__time">9 pm</span>Dancing</li>
  </ul>
</section>

<section class="card menu">
  <h2 class="script-cocoa menu__title">Dinner<br>Menu</h2>
  <ul class="menu__courses">
    <li class="menu__course">Salad</li>
    <li class="menu__course">Soup</li>
    <li class="menu__course">Mine</li>
    <li class="menu__course">Dessert</li>
  </ul>
  <div class="floral floral--bouquet" role="img" aria-label="Small watercolour arrangement of pink roses and leaves"></div>
</section>

<div class="tag tag--back">
  <span class="tag__monogram">R&amp;M</span>
</div>
<div class="tag tag--front">
  <span class="tag__hole"></span>
  <p class="script-pink tag__headline">Save<br>the<br>Date</p>
  <div class="floral floral--sprig" role="img" aria-label="Watercolour leaf sprig"></div>
</div>
<svg class="tag__bow" viewBox="0 0 62 48" aria-hidden="true">
  <path d="M31 20 C20 6 6 8 10 18 C13 26 24 24 31 20 Z M31 20 C42 6 56 8 52 18 C49 26 38 24 31 20 Z" fill="none" stroke="var(--blush)" stroke-width="3"/>
  <path d="M31 20 L22 46 M31 20 L40 44" stroke="var(--blush)" stroke-width="3" fill="none" stroke-linecap="round"/>
  <circle cx="31" cy="20" r="4" fill="var(--blush)"/>
</svg>

<section class="card thanks">
  <h2 class="script-cocoa thanks__title">Thank<br>you</h2>
  <div class="floral floral--bouquet" role="img" aria-label="Small watercolour pink roses with leaves"></div>
</section>

</body>
</html>
```